Edgy rebranded biz cards KRB

We are rebranding our 20 yr old mortgage company with a new logo and would like cards to compliment our new look.

Target Market(s)

potential home buyers or clients for refinance

Industry/Entity Type

Mortgage Brokerage

Contact Information for Business Card

418 W. Lomita Ave #305
Henderson, NV 89152
702.519.4827 o
702-519-4829 f
www.kestrelridgelending,example
nmls 842019
KRB is an equal housing lender

Font styles to use
Sans Serif

Colors
0455a3
3176b5
0393ce
33a6d7

Requirements
Must have
• space for a photo
Nice to have
• One side with the company info and the other with the person's info

```html
<!DOCTYPE html>
<html lang="en">
<head>
<meta charset="utf-8">
<title>Kestrel Ridge Lending — Business Cards</title>
<link rel="stylesheet" href="https://fonts.googleapis.com/css2?family=Montserrat:wght@600;700&family=Nunito+Sans:wght@400;600&display=swap">
<style>
  :root {
    --page: #cccccc;
    --navy: #0455a3;
    --mid: #3176b5;
    --bright: #0393ce;
    --sky: #33a6d7;
    --ink: #333333;
    --muted: #7a7a7a;
    --name: #0566b5;
    --white: #ffffff;
  }
  * { box-sizing: border-box; margin: 0; padding: 0; }
  html, body { width: 1062px; height: 1200px; overflow: hidden; background: var(--page); }
  .sheet { position: relative; width: 1062px; height: 1200px; }

  .card {
    position: absolute; left: 146px; width: 806px; height: 460px;
    overflow: hidden; background: var(--white);
  }
  .card--company { top: 78px; }
  .card--person { top: 587px; height: 461px; }

  .card__shapes { position: absolute; inset: 0; width: 100%; height: 100%; }

  .skyline {
    position: absolute; left: 0; bottom: 0; width: 500px; height: 140px;
    background: linear-gradient(180deg, rgba(4,85,163,0) 0%, rgba(4,85,163,0.18) 100%);
  }

  .brand {
    position: absolute; left: 24px; width: 390px; text-align: center;
    font-family: "Montserrat", sans-serif; font-weight: 700; color: var(--white);
  }
  .brand__name { font-size: 44px; line-height: 1; letter-spacing: -0.5px; }
  .brand__sub { font-size: 26px; line-height: 1; margin-top: 10px; letter-spacing: 1px; }
  .card--company .brand { top: 140px; }
  .card--person .brand { top: 140px; }

  .contact { position: absolute; font-family: "Nunito Sans", sans-serif; font-size: 13.5px; color: var(--ink); }
  .contact__row { position: absolute; left: 0; display: flex; align-items: center; white-space: nowrap; }
  .contact__icon {
    width: 36px; height: 36px; border-radius: 50%; background: var(--sky);
    display: flex; align-items: center; justify-content: center; flex: none;
  }
  .contact__icon svg { width: 18px; height: 18px; }
  .contact__text { line-height: 19.5px; }

  .card--company .contact { left: 531px; top: 0; }
  .card--company .contact__text { margin-left: 14px; }
  .card--person .contact { left: 548px; top: 0; }
  .card--person .contact__text { margin-left: 14px; line-height: 21px; }

  .portrait {
    position: absolute; left: 551px; top: 49px; width: 95px; height: 90px;
    border: 1.5px solid var(--sky); padding: 4px; background: var(--white);
  }
  .portrait__fill {
    width: 100%; height: 100%;
    background: radial-gradient(ellipse at 50% 90%, #2a2d33 0%, #3d4046 35%, #8e8f92 65%, #a3a4a6 100%);
  }

  .person { position: absolute; left: 551px; top: 152px; }
  .person__name {
    font-family: "Montserrat", sans-serif; font-weight: 700; font-size: 20.5px;
    color: var(--name); letter-spacing: 0.8px; white-space: nowrap;
  }
  .person__role {
    font-family: "Nunito Sans", sans-serif; font-size: 14px; color: var(--muted);
    letter-spacing: 2px; margin-top: 4px;
  }
</style>
</head>
<body>
<main class="sheet">

  <!-- Company side -->
  <section class="card card--company">
    <svg class="card__shapes" viewBox="0 0 806 460" preserveAspectRatio="none" aria-hidden="true">
      <defs>
        <linearGradient id="blueFade1" x1="0" y1="0" x2="0" y2="1">
          <stop offset="0" stop-color="#0455a3"/>
          <stop offset="0.45" stop-color="#0470ba"/>
          <stop offset="1" stop-color="#0393ce"/>
        </linearGradient>
      </defs>
      <rect width="806" height="460" fill="url(#blueFade1)"/>
      <polygon points="554,0 416,229 554,460 806,460 806,0" fill="#ffffff"/>
      <polygon points="461,0 554,0 519,58" fill="#33a6d7"/>
      <polygon points="464,460 520,404 554,460" fill="#0455a3"/>
    </svg>
    <div class="skyline" role="img" aria-label="Faint line drawing of a city street with buildings and trees"></div>

    <div class="brand">
      <div class="brand__name">KESTREL RIDGE</div>
      <div class="brand__sub">LENDING</div>
    </div>

    <div class="contact">
      <div class="contact__row" style="top:105px;">
        <span class="contact__icon"><svg viewBox="0 0 24 24"><path d="M12 2a7 7 0 0 0-7 7c0 5 7 13 7 13s7-8 7-13a7 7 0 0 0-7-7zm0 9.5A2.5 2.5 0 1 1 12 6.5a2.5 2.5 0 0 1 0 5z" fill="#fff"/></svg></span>
        <span class="contact__text">418 W. Lomita Ave #305<br>Henderson, NV 89152</span>
      </div>
      <div class="contact__row" style="top:173px;">
        <span class="contact__icon"><svg viewBox="0 0 24 24"><rect x="9" y="3" width="10" height="18" rx="2" fill="#fff"/><rect x="4" y="7" width="4" height="12" rx="2" fill="#fff"/><g fill="#33a6d7"><rect x="11" y="5" width="6" height="3"/><rect x="11" y="10" width="1.6" height="1.6"/><rect x="13.2" y="10" width="1.6" height="1.6"/><rect x="15.4" y="10" width="1.6" height="1.6"/><rect x="11" y="13" width="1.6" height="1.6"/><rect x="13.2" y="13" width="1.6" height="1.6"/><rect x="15.4" y="13" width="1.6" height="1.6"/></g></svg></span>
        <span class="contact__text">OFFICE: 702.519.4827 O</span>
      </div>
      <div class="contact__row" style="top:234px;">
        <span class="contact__icon"><svg viewBox="0 0 24 24"><path d="M9 3h7l3 3v6H9z" fill="#fff"/><rect x="4" y="11" width="16" height="10" rx="1.5" fill="#fff"/><rect x="6" y="14" width="2" height="2" fill="#33a6d7"/><rect x="6" y="17" width="2" height="2" fill="#33a6d7"/></svg></span>
        <span class="contact__text">FAX: 702-519-4829</span>
      </div>
      <div class="contact__row" style="top:295px; align-items:flex-start;">
        <span class="contact__icon"><svg viewBox="0 0 24 24" fill="none" stroke="#fff" stroke-width="1.6"><circle cx="12" cy="12" r="9"/><ellipse cx="12" cy="12" rx="4" ry="9"/><path d="M3 12h18M4.5 7.5h15M4.5 16.5h15"/></svg></span>
        <span class="contact__text">www.kestrelridgelending,example<br>nmls 842019 &nbsp;|<br>KRB is an equal housing lender</span>
      </div>
    </div>
  </section>

  <!-- Personal side -->
  <section class="card card--person">
    <svg class="card__shapes" viewBox="0 0 806 461" preserveAspectRatio="none" aria-hidden="true">
      <defs>
        <linearGradient id="blueFade2" x1="0" y1="0" x2="0" y2="1">
          <stop offset="0" stop-color="#0455a3"/>
          <stop offset="0.45" stop-color="#0470ba"/>
          <stop offset="1" stop-color="#0393ce"/>
        </linearGradient>
      </defs>
      <rect width="806" height="461" fill="url(#blueFade2)"/>
      <polygon points="556,0 400,217 575,461 806,461 806,0" fill="#ffffff"/>
      <polygon points="421,0 556,0 500,79" fill="#33a6d7"/>
      <polygon points="474,461 533,402 575,461" fill="#0455a3"/>
    </svg>
    <div class="skyline" role="img" aria-label="Faint line drawing of a city street with buildings and trees"></div>

    <div class="brand">
      <div class="brand__name">KESTREL RIDGE</div>
      <div class="brand__sub">LENDING</div>
    </div>

    <div class="portrait"><div class="portrait__fill" role="img" aria-label="Portrait photo of the loan officer in a dark suit against a grey backdrop"></div></div>

    <div class="person">
      <div class="person__name">DANIEL OSTROW M.S</div>
      <div class="person__role">OWNER</div>
    </div>

    <div class="contact">
      <div class="contact__row" style="top:218px;">
        <span class="contact__icon"><svg viewBox="0 0 24 24"><path d="M12 2a7 7 0 0 0-7 7c0 5 7 13 7 13s7-8 7-13a7 7 0 0 0-7-7zm0 9.5A2.5 2.5 0 1 1 12 6.5a2.5 2.5 0 0 1 0 5z" fill="#fff"/></svg></span>
        <span class="contact__text">418 W. Lomita Ave #305<br>Henderson, NV 89152</span>
      </div>
      <div class="contact__row" style="top:275px;">
        <span class="contact__icon"><svg viewBox="0 0 24 24"><rect x="9" y="3" width="10" height="18" rx="2" fill="#fff"/><rect x="4" y="7" width="4" height="12" rx="2" fill="#fff"/><g fill="#33a6d7"><rect x="11" y="5" width="6" height="3"/><rect x="11" y="10" width="1.6" height="1.6"/><rect x="13.2" y="10" width="1.6" height="1.6"/><rect x="15.4" y="10" width="1.6" height="1.6"/><rect x="11" y="13" width="1.6" height="1.6"/><rect x="13.2" y="13" width="1.6" height="1.6"/><rect x="15.4" y="13" width="1.6" height="1.6"/></g></svg></span>
        <span class="contact__text">OFFICE: 702.519.4827 O</span>
      </div>
      <div class="contact__row" style="top:325px;">
        <span class="contact__icon"><svg viewBox="0 0 24 24"><path d="M9 3h7l3 3v6H9z" fill="#fff"/><rect x="4" y="11" width="16" height="10" rx="1.5" fill="#fff"/><rect x="6" y="14" width="2" height="2" fill="#33a6d7"/><rect x="6" y="17" width="2" height="2" fill="#33a6d7"/></svg></span>
        <span class="contact__text">FAX: 702-519-4829</span>
      </div>
    </div>
  </section>

</main>
</body>
</html>
```